K.T.L Services

We are needing business cards for a construction company that does everything from painting and detailing, maintenance, Sheetrock repairs, demolition, tile and wood floors. Also, K.T.L stands for Detailing, maintenance, and Painting. We would like the colors to be closer to the colors grey and light brown/khaki, but if there is any other suggestions that would go better with the design we are open to ideas.

Industry/Entity Type

Business

Contact Information for Business Card

Owner / Operator Owen Tallis (555) 412-3907 / (555) 738- 2164

Font styles to use
Sans Serif

```html
<!DOCTYPE html>
<html lang="en">
<head>
<meta charset="utf-8">
<title>K.T.L Services – Business Card</title>
<link href="https://fonts.googleapis.com/css2?family=Marcellus&display=swap" rel="stylesheet">
<style>
  :root {
    --page: #ebe8e2;
    --paper: #ffffff;
    --paper-shade: #eeeeee;
    --khaki-light: #d3bd93;
    --khaki: #b9a176;
    --khaki-dark: #9c8660;
    --grey-band: #c4c4c4;
    --gold-text: #c3a975;
    --ink-light: #ffffff;
  }
  * { margin: 0; padding: 0; box-sizing: border-box; }
  html, body {
    width: 1200px; height: 780px; overflow: hidden;
    background: var(--page);
    font-family: "Marcellus", "Optima", sans-serif;
  }
  .sheet {
    width: 1200px; height: 780px;
    display: flex; align-items: center; justify-content: center; gap: 40px;
  }
  .card {
    position: relative;
    width: 540px; height: 309px;
    border-radius: 3px;
    overflow: hidden;
    box-shadow: 0 10px 26px rgba(60, 50, 30, 0.22);
  }
  .card-front { background: linear-gradient(135deg, var(--paper), var(--paper-shade)); }
  .front-art { position: absolute; inset: 0; width: 100%; height: 100%; }

  .brand {
    position: absolute; left: 28px; top: 124px;
    display: flex; align-items: center; gap: 12px;
  }
  .brand-mark {
    width: 52px; height: 52px; border-radius: 50%;
    background: var(--grey-band);
    flex: none;
  }
  .brand-name {
    color: var(--gold-text);
    font-size: 24px; line-height: 1;
    white-space: nowrap;
  }

  .details {
    position: absolute; left: 336px; top: 38px; right: 18px;
    color: var(--ink-light);
  }
  .company { font-size: 27px; font-weight: 400; letter-spacing: 0.5px; margin-bottom: 22px; white-space: nowrap; }
  .person { font-size: 20px; }
  .role { font-size: 14px; margin-bottom: 14px; }
  .phone {
    display: flex; align-items: center; gap: 8px;
    font-size: 15px; margin-bottom: 5px; white-space: nowrap;
  }
  .phone-icon { width: 15px; height: 15px; flex: none; }

  .card-back {
    background: linear-gradient(135deg, var(--khaki-light), var(--khaki) 55%, var(--khaki-dark));
    display: flex; align-items: center; justify-content: center;
  }
  .back-name { color: var(--ink-light); font-size: 40px; letter-spacing: 1px; }
</style>
</head>
<body>
<main class="sheet">
  <section class="card card-front" aria-label="Business card front">
    <svg class="front-art" viewBox="0 0 540 309" preserveAspectRatio="none" aria-hidden="true">
      <defs>
        <linearGradient id="khakiPanel" x1="0" y1="0" x2="1" y2="1">
          <stop offset="0" stop-color="#d6c198"/>
          <stop offset="0.6" stop-color="#bba377"/>
          <stop offset="1" stop-color="#a38c64"/>
        </linearGradient>
      </defs>
      <path class="band-grey" d="M292 0 C 300 110, 330 190, 420 240 C 470 268, 500 290, 520 309 L540 309 L540 0 Z" fill="#c4c4c4"/>
      <path class="band-khaki" d="M306 0 C 316 100, 346 176, 432 224 C 480 250, 512 276, 540 300 L540 0 Z" fill="url(#khakiPanel)"/>
    </svg>

    <div class="brand">
      <span class="brand-mark" aria-hidden="true"></span>
      <p class="brand-name">K.T.L Services</p>
    </div>

    <div class="details">
      <h1 class="company">K.T.L Services</h1>
      <p class="person">Owen Tallis</p>
      <p class="role">Owner / Operator</p>
      <p class="phone">
        <svg class="phone-icon" viewBox="0 0 16 16" aria-hidden="true">
          <rect x="0.5" y="0.5" width="15" height="15" rx="2" fill="#ffffff"/>
          <path d="M4.5 3.5 L6.5 3.5 L7.3 6 L6 7 Q7 9.2 9 10 L10 8.7 L12.5 9.5 L12.5 11.5 Q7.5 12 4.5 7 Z" fill="#b9a176"/>
        </svg>
        (555) 412-3907
      </p>
      <p class="phone">
        <svg class="phone-icon" viewBox="0 0 16 16" aria-hidden="true">
          <rect x="0.5" y="0.5" width="15" height="15" rx="2" fill="#ffffff"/>
          <path d="M4.5 3.5 L6.5 3.5 L7.3 6 L6 7 Q7 9.2 9 10 L10 8.7 L12.5 9.5 L12.5 11.5 Q7.5 12 4.5 7 Z" fill="#b9a176"/>
        </svg>
        (555) 738- 2164
      </p>
    </div>
  </section>

  <section class="card card-back" aria-label="Business card back">
    <p class="back-name">K.T.L Services</p>
  </section>
</main>
</body>
</html>
```